B2B telecom company need web design

We need a web design for our corporate web site. The company exists since almost 10 years.
This is a DESIGN contest, you're expected to provide design only, NOT the whole website. The winner will have to provide the HTML template (with Lorem Ipsum content) and the CSS files of his design.
Our initial product is SMS peering in P2P (you send a SMS to a friend in a foreign country, great chance that your operator route your SMS to us that we route to the recipient). We're launching a bulk SMS service (marketing and application to SMS).
Target is mostly corporate, usually big corporate (operators, contents providers...) where use of SMS is part of the main business.
The web site is composed of 1 landing page and 7 content pages (plan is given for your information, all content page are using the same template and the same design, you do NOT need to make one design per page) :
* About US
Company Profile
They trust us
The Volnor Team
Partners
Contact us
* Solution
P2P SMS
A2P SMS
You only need to submit the landing page and a template page for the content (with h1, h2, h3 and h4).
Design must be based on our new logo (see attached file).
Our current web site http://www.volnor-example.com
The winner of the contest will have to provide state of the art HTML template and CSS files of his design. Photo used shall be downloaded from Pixelbrook (provide the ID of the picture that we purchase file).
Target Market(s)
Telecom operator. SMS Peering hubs. Bulk SMS.
Industry/Entity Type
It Company
Number of Pages Required
2 page

```html
<!DOCTYPE html>
<html lang="en">
<head>
<meta charset="utf-8">
<title>Volnor Mobile</title>
<link rel="stylesheet" href="https://fonts.googleapis.com/css2?family=Oswald:wght@300;400;500;700&family=Open+Sans:wght@400;600&display=swap">
<style>
:root{
  --green:#7ab51d;
  --green-dark:#4f7d12;
  --ink:#1e1e1e;
  --text:#555;
  --line:#d6d6d6;
  --partner:#1d2f6b;
  --footer:#2f333d;
  --footer-text:#b9bcc4;
  --footer-line:#5a5f6b;
  --white:#fff;
}
*{margin:0;padding:0;box-sizing:border-box}
html,body{width:1200px;height:2609px;overflow:hidden;background:var(--white)}
body{position:relative;font-family:"Open Sans",Arial,sans-serif;color:var(--text)}
.abs{position:absolute}
.topbar{left:0;top:0;width:1200px;height:4px;background:var(--green)}
.regions{left:579px;top:4px;width:438px;height:43px;border:1px solid var(--line);border-top:none;display:flex;font-family:"Oswald",sans-serif;font-size:11px;color:#444}
.regions div{flex:1;text-align:right;padding:5px 14px 0 0;line-height:16px}
.regions div+div{border-left:1px solid var(--line)}
.brand{left:183px;top:64px;font-family:"Oswald",sans-serif;font-weight:400;font-size:23px;color:#333;letter-spacing:1px}
.nav{left:428px;top:69px;display:flex;align-items:center;font-family:"Oswald",sans-serif;font-size:12px;color:#444;text-transform:uppercase}
.nav a{color:inherit;text-decoration:none;padding:3px 10px}
.nav a.active{background:var(--green);color:var(--white)}
.nav i{width:1px;height:12px;background:#aaa;margin:0 8px}
.hero{left:0;top:115px;width:1200px;height:438px;background:radial-gradient(ellipse at 50% 70%,#f4f4f4 0%,#bdbdbd 45%,#7c7c7c 100%)}
.hero-text{left:0;top:245px;width:1200px;text-align:center;font-family:"Oswald",sans-serif;color:var(--white);text-transform:uppercase}
.hero-text h1{font-size:73px;font-weight:700;line-height:80px;text-shadow:0 2px 4px rgba(0,0,0,.3)}
.hero-text .l2{font-size:36px;font-weight:700;line-height:42px;text-shadow:0 2px 3px rgba(0,0,0,.3)}
.hero-text .l3{font-size:50px;font-weight:300;color:#222;letter-spacing:5px;line-height:56px}
.arrow{width:28px;height:28px;top:320px}
.dots{left:573px;top:514px;display:flex;gap:6px}
.dots span{width:8px;height:8px;border-radius:50%;background:var(--white)}
.dots span.on{background:var(--green)}
.title{left:0;width:1200px;text-align:center;font-family:"Oswald",sans-serif;font-size:32px;font-weight:400;color:var(--ink);text-transform:uppercase}
.card{top:666px;width:319px;height:221px;border:1px solid var(--line);text-align:center}
.card .icon{display:block;margin:16px auto 0;width:94px;height:94px}
.card h3{font-family:"Oswald",sans-serif;font-weight:400;font-size:19px;color:var(--ink);margin-top:6px}
.card p{font-size:12px;line-height:19px;margin:6px 40px 0}
.profile{left:252px;top:1008px;width:686px;list-style:none}
.profile li{position:relative;padding:4px 0 11px 14px;font-size:11px;line-height:17px;border-bottom:1px solid var(--line);margin-bottom:8px}
.profile li:last-child{border-bottom:none}
.profile li::before{content:"";position:absolute;left:0;top:10px;width:6px;height:6px;border-radius:50%;background:var(--green)}
.member{top:1474px;width:184px;text-align:center}
.member .photo{margin:0 auto;width:118px;height:118px;border-radius:50%;border:4px solid var(--green);background:radial-gradient(circle at 50% 40%,#9a9a9a,#3c3c3c)}
.member h4{font-family:"Oswald",sans-serif;font-weight:500;font-size:14px;color:var(--green);margin-top:14px}
.member p{font-size:12px;line-height:18px;margin-top:6px}
.member a{display:inline-block;margin-top:20px;background:var(--green);color:var(--white);font-family:"Oswald",sans-serif;font-size:11px;padding:4px 10px;text-decoration:none}
.sep{top:1520px;width:2px;height:30px;background:var(--green)}
.partner{width:214px;height:95px;border-bottom:1px solid var(--line)}
.partner.last{border-bottom:none}
.partner .mark{font-family:"Oswald",sans-serif;font-weight:700;font-size:30px;color:var(--partner);margin-top:18px;display:flex;align-items:center;gap:8px}
.partner .mark i{width:18px;height:18px;background:var(--partner);border-radius:50%}
.partner small{display:block;font-size:11px;color:#333;margin-top:4px}
.footer{left:0;top:2195px;width:1200px;height:414px;background:var(--footer);color:var(--footer-text)}
.footer h5{position:absolute;font-family:"Oswald",sans-serif;font-weight:400;font-size:16px;color:var(--white);text-transform:uppercase;padding-bottom:8px;border-bottom:1px solid var(--footer-line)}
.footer p.about{position:absolute;left:186px;top:100px;width:447px;font-size:9.5px;line-height:17.5px}
.offices{position:absolute;left:722px;top:101px;font-family:"Oswald",sans-serif;font-weight:300;font-size:15px;line-height:25px}
.offices b{color:var(--green);font-weight:500}
.links{position:absolute;top:292px;list-style:none;font-size:10px;line-height:17.5px}
.flogo{position:absolute;left:722px;top:250px;font-family:"Oswald",sans-serif;font-weight:400;font-size:21px;color:var(--white);letter-spacing:1px}
.copy{position:absolute;left:722px;top:290px;font-size:10px;color:var(--white);font-weight:600}
</style>
</head>
<body>
<div class="abs topbar"></div>
<div class="abs regions">
  <div>Asia • Australia<br>Email Contact : apac@volnor-example.com</div>
  <div>Europe • Middle East • Africa<br>Email Contact : emea@volnor-example.com</div>
</div>
<div class="abs brand">VOLNOR MOBILE</div>
<nav class="abs nav">
  <a class="active">About Us</a><i></i><a>Company Profile</a><i></i><a>They Trust Us</a><i></i><a>The Volnor Team</a><i></i><a>Partners</a><i></i><a>Contact Us</a>
</nav>

<section class="abs hero" role="img" aria-label="Grey world map with network lines and a globe grid"></section>
<div class="abs hero-text">
  <h1>Volnor-Mobile</h1>
  <div class="l2">Enables Global SMS Connectivity</div>
  <div class="l3">In Both A2P and PSP</div>
</div>
<svg class="abs arrow" style="left:181px" viewBox="0 0 28 28"><circle cx="14" cy="14" r="14" fill="#7ab51d"/><path d="M16 9l-5 5 5 5" stroke="#fff" stroke-width="2.5" fill="none"/></svg>
<svg class="abs arrow" style="left:991px" viewBox="0 0 28 28"><circle cx="14" cy="14" r="14" fill="#7ab51d"/><path d="M12 9l5 5-5 5" stroke="#fff" stroke-width="2.5" fill="none"/></svg>
<div class="abs dots"><span class="on"></span><span></span><span></span><span></span></div>

<h2 class="abs title" style="top:586px">Solutions We Provide</h2>
<div class="abs card" style="left:263px">
  <svg class="icon" viewBox="0 0 94 94"><circle cx="47" cy="47" r="46" fill="#4f7d12"/><circle cx="47" cy="47" r="38" fill="#7ab51d"/><path d="M30 34h26v18H40l-6 6v-6h-4z" fill="#fff"/><path d="M60 40h5v16h-4v5l-5-5H44v-2h16z" fill="#fff"/></svg>
  <h3>P2P SMS</h3>
  <p>Lorem Ipsum is simply dummy text of the printing and typesetting industry.</p>
</div>
<div class="abs card" style="left:617px">
  <svg class="icon" viewBox="0 0 94 94"><circle cx="47" cy="47" r="46" fill="#4f7d12"/><circle cx="47" cy="47" r="38" fill="#7ab51d"/><rect x="34" y="26" width="26" height="42" rx="4" fill="#fff"/><rect x="38" y="40" width="18" height="12" fill="#7ab51d"/><path d="M38 40l9 7 9-7" stroke="#fff" stroke-width="1.5" fill="none"/></svg>
  <h3>A2P SMS</h3>
  <p>Lorem Ipsum is simply dummy text of the printing and typesetting industry.</p>
</div>

<h2 class="abs title" style="top:932px">Company Profile</h2>
<ul class="abs profile">
  <li>In 2007, Corvane 365, the global leader in mobile messaging, announced the launch of the Africa and Middle East Exchange (VOLNOR Mobile Exchange) mobile messaging hub, to consolidate its position as the major provider of international SMS across Africa and the Middle East .</li>
  <li>The new Hub allows to expand further into this fast-growing region and offer international SMS services to more than 250 million subscribers.</li>
  <li>Today, as an independent company VOLNOR can be characterized as the combination of world-class enterprise solutions and an unrivaled global data network, creating the Middle East &amp; Africa foremost provider of mobile messaging. The result for our customers is unlimited potential.</li>
  <li>VOLNOR has now evolved into a global company offering wide range of our solutions and enables Mobile Operators &amp; Enterprises connecting their subscribers to the wider international mobile community in 83 countries connected to 900 Mobile Networks Globally.</li>
  <li>VOLNOR Mobile Exchange with its Partners, has the resources, presence, knowledge and experience to improve the efficiency of your operations with faith, team spirit and enthusiasm to achieve your goal.</li>
</ul>

<h2 class="abs title" style="top:1398px">Volnor Teams</h2>
<div class="abs member" style="left:230px"><div class="photo" role="img" aria-label="Portrait photo of team member"></div><h4>NAME</h4><p>Lorem Ipsum is simply dummy text of the printing industry.</p><a>READ MORE</a></div>
<div class="abs sep" style="left:414px"></div>
<div class="abs member" style="left:414px"><div class="photo" role="img" aria-label="Portrait photo of team member"></div><h4>NAME</h4><p>Lorem Ipsum is simply dummy text of the printing industry.</p><a>READ MORE</a></div>
<div class="abs sep" style="left:598px"></div>
<div class="abs member" style="left:598px"><div class="photo" role="img" aria-label="Portrait photo of team member"></div><h4>NAME</h4><p>Lorem Ipsum is simply dummy text of the printing industry.</p><a>READ MORE</a></div>
<div class="abs sep" style="left:782px"></div>
<div class="abs member" style="left:781px"><div class="photo" role="img" aria-label="Portrait photo of team member"></div><h4>NAME</h4><p>Lorem Ipsum is simply dummy text of the printing industry.</p><a>READ MORE</a></div>

<h2 class="abs title" style="top:1786px">Partner of Volnor</h2>
<div class="abs partner" style="left:367px;top:1860px"><div class="mark">Quantiro</div><small>Quantiro</small></div>
<div class="abs partner" style="left:620px;top:1860px"><div class="mark"><i></i>Harborlink</div><small>Harborlink</small></div>
<div class="abs partner" style="left:367px;top:1955px"><div class="mark">Meridex</div><small>Meridex</small></div>
<div class="abs partner" style="left:620px;top:1955px"><div class="mark">Tallwave</div><small>Tallwave</small></div>
<div class="abs partner last" style="left:367px;top:2050px"><div class="mark">Brightnode</div><small>Brightnode</small></div>
<div class="abs partner last" style="left:620px;top:2050px"><div class="mark"><i></i>Ferrowin</div><small>Ferrowin</small></div>

<footer class="abs footer">
  <h5 style="left:186px;top:50px;width:447px">About Us</h5>
  <p class="about">Lorem Ipsum is simply dummy text of the printing and typesetting industry. Lorem Ipsum has been the industry's standard dummy text ever since the 1500s, when an unknown printer took a galley of type and scrambled it to make a type specimen book. It has survived not only five centuries, but also the leap into electronic typesetting, remaining essentially unchanged. It was popularised in the 1960s with the release of Typeleaf sheets containing Lorem Ipsum passages, and more recently with desktop publishing software like Pagewright Studio including versions of Lorem Ipsum.</p>
  <h5 style="left:722px;top:50px;width:298px">Global Sales Offices</h5>
  <div class="offices"><b>Address:</b> Headquarters (Geneva - Switzerland)<br>Rue des Tilleuls 14 CH-1201 Geneva<br><b>Phone:</b> +41 22 555 01 37<br><b>Email Contact :</b> info@volnor-example.com</div>
  <h5 style="left:186px;top:240px;width:136px">Get Started</h5>
  <h5 style="left:339px;top:240px;width:136px">Help</h5>
  <h5 style="left:492px;top:240px;width:140px">Company</h5>
  <ul class="links" style="left:186px"><li>How it Works</li><li>Our Pricing</li><li>Why Us?</li></ul>
  <ul class="links" style="left:339px"><li>FAQ's</li><li>Packing Tips</li><li>Contact us</li></ul>
  <ul class="links" style="left:492px"><li>About Us</li><li>Services</li><li>Blog Posts</li></ul>
  <div class="flogo">VOLNOR MOBILE</div>
  <div class="copy">© 2015 VOLNOR Mobile. All rights reserved.</div>
</footer>
</body>
</html>
```